Quarvex Power Point Template - Institutional Presentation

Develop a comprehensive template for a corporate presentation power point.

The presentation will be aimed to institutional investors.

Style to be modern and contemporary. Use of icons and images welcome but not to much.

It would be great if you could develop the layout/style for the content in the following slides:

- Cover
- Section title
- Slide with title and bullet points on one side and two text boxes on the other side
- Slide with line chart and pie chart
- Slide with table

Should we like the slides above we will then develop the rest of the template.

We may then need to have a dark-background version - but this will be invoiced separately.

Target Market(s)

Corporate institutional investors

Industry/Entity Type

Finance

Font styles to use
Serif
Sans Serif

Colors
3176b5
0255a3
cee9f5
86cae7
33a6d7
0792cd
33b8a4
00a990
86cfc6

Requirements
Must have
• Mostly white background with minimal objects
Nice to have
• Use of photos, but not to much.

```html
<!DOCTYPE html>
<html lang="en">
<head>
<meta charset="utf-8">
<title>Quarvex Slide Design Idea 02</title>
<link href="https://fonts.googleapis.com/css2?family=Arimo:wght@400;700&display=swap" rel="stylesheet">
<style>
:root{
  --backdrop:#3b1313;
  --sheet:#ffffff;
  --caption:#7d6c6c;
  --label:#333333;
  --navy:#1f3a6e;
  --blue:#2f8fd0;
  --sky:#33a6d7;
  --orange:#f29a1f;
  --red:#e0452b;
  --green:#8bc34a;
  --teal:#1aa58a;
  --yellow:#f5c518;
  --purple:#8e44ad;
  --grey:#d9d9d9;
  --ink:#666666;
}
*{box-sizing:border-box;margin:0;padding:0}
html,body{width:1200px;height:930px;overflow:hidden}
body{background:var(--backdrop);font-family:"Arimo",Arial,sans-serif;position:relative}
.sheet{position:absolute;background:var(--sheet)}
.sheet-main{left:114px;top:27px;width:1008px;height:755px}
.sheet-tail{left:114px;top:782px;width:176px;height:128px}
.slide{position:absolute;width:140px;height:104px;box-shadow:0 1px 3px rgba(0,0,0,.35);background:#fff}
.slide svg{display:block;width:140px;height:104px}
.file-name{position:absolute;width:140px;text-align:center;font-size:8.5px;color:var(--label)}
.collection-title{position:absolute;left:330px;width:690px;top:818px;text-align:center;color:var(--caption);font-weight:700;font-size:26px;line-height:33px}
.fill-blue{fill:var(--blue)}.fill-sky{fill:var(--sky)}.fill-orange{fill:var(--orange)}.fill-red{fill:var(--red)}
.fill-green{fill:var(--green)}.fill-teal{fill:var(--teal)}.fill-yellow{fill:var(--yellow)}.fill-navy{fill:var(--navy)}
.fill-purple{fill:var(--purple)}.fill-grey{fill:var(--grey)}
.heading{font-size:6px;fill:var(--ink)}
.subhead{font-size:5.5px;fill:var(--ink);text-anchor:middle}
.cover-text{font-size:4.5px;fill:#fff;font-weight:700;text-anchor:middle}
.brand-word{font-size:4.2px;font-weight:700;fill:var(--navy)}
.figure{font-size:10px;fill:#fff}
.big-pct{font-size:9px;fill:var(--teal)}
.txt{fill:var(--grey)}
</style>
</head>
<body>
<svg width="0" height="0" style="position:absolute" aria-hidden="true">
  <defs>
    <linearGradient id="rainbow" x1="0" x2="1">
      <stop offset="0" stop-color="#2f8fd0"/><stop offset=".25" stop-color="#f5c518"/>
      <stop offset=".5" stop-color="#8bc34a"/><stop offset=".75" stop-color="#e0452b"/><stop offset="1" stop-color="#2f8fd0"/>
    </linearGradient>
    <linearGradient id="dusk" x1="0" y1="0" x2="0" y2="1">
      <stop offset="0" stop-color="#e8a45c"/><stop offset=".5" stop-color="#9aa6b3"/><stop offset="1" stop-color="#3d4f66"/>
    </linearGradient>
    <linearGradient id="tower" x1="0" y1="0" x2="1" y2="1">
      <stop offset="0" stop-color="#b9cfe6"/><stop offset=".6" stop-color="#4f78a8"/><stop offset="1" stop-color="#23406c"/>
    </linearGradient>
    <linearGradient id="mosaic" x1="0" x2="1">
      <stop offset="0" stop-color="#e98c3a"/><stop offset=".5" stop-color="#5a6f8a"/><stop offset="1" stop-color="#4a90d9"/>
    </linearGradient>
    <symbol id="chrome" viewBox="0 0 175 130">
      <rect width="175" height="130" fill="#fff"/>
      <rect x="9" y="15" width="157" height=".8" fill="url(#rainbow)"/>
      <rect x="138" y="6" width="4" height="4" class="fill-navy"/>
      <text x="144" y="10" class="brand-word">QUARVEX</text>
      <rect x="25" y="111" width="125" height="1" class="txt"/>
      <rect x="40" y="114" width="95" height="1" class="txt"/>
      <rect x="9" y="121" width="157" height=".8" fill="url(#rainbow)"/>
    </symbol>
  </defs>
</svg>

<div class="sheet sheet-main"></div>
<div class="sheet sheet-tail"></div>

<!-- Row 1 -->
<div class="slide" style="left:126px;top:38px"><svg viewBox="0 0 175 130">
  <rect width="175" height="130" fill="#fff"/>
  <rect width="175" height="75" fill="url(#mosaic)" role="img" aria-label="City skyline photo framed by orange and blue tiles"/>
  <text x="87" y="90" class="subhead" style="font-size:5px">ENTER YOUR PRESENTATION TITLE</text>
  <rect x="76" y="99" width="4" height="4" class="fill-navy"/><text x="82" y="103" class="brand-word">QUARVEX</text>
</svg></div>
<div class="slide" style="left:295px;top:38px"><svg viewBox="0 0 175 130">
  <rect width="175" height="130" fill="url(#tower)" role="img" aria-label="Skyscraper and city street photo"/>
  <rect width="175" height="14" fill="#fff"/>
  <text x="87" y="10" class="brand-word" text-anchor="middle">QUARVEX</text>
  <polygon points="10,66 165,58 160,88 10,94" fill="#2a4f8f"/>
  <text x="87" y="74" class="cover-text">ENTER YOUR</text><text x="87" y="81" class="cover-text">PRESENTATION TITLE</text>
</svg></div>
<div class="slide" style="left:465px;top:38px"><svg viewBox="0 0 175 130">
  <rect width="175" height="130" fill="url(#dusk)" role="img" aria-label="City skyline at sunset photo"/>
  <circle cx="87" cy="58" r="27" fill="#fff"/>
  <text x="87" y="60" class="brand-word" text-anchor="middle">QUARVEX</text>
  <polygon points="10,104 165,98 165,124 10,124" fill="#2a4f8f"/>
  <text x="87" y="111" class="cover-text">ENTER YOUR</text><text x="87" y="118" class="cover-text">PRESENTATION TITLE</text>
</svg></div>
<div class="slide" style="left:634px;top:38px"><svg viewBox="0 0 175 130">
  <rect width="175" height="130" fill="url(#tower)" role="img" aria-label="Glass tower against sky photo"/>
  <rect width="175" height="60" fill="#1f4a8f"/>
  <text x="87" y="20" class="cover-text">ENTER YOUR PRESENTATION TITLE</text>
  <circle cx="87" cy="62" r="27" fill="#fff"/>
  <text x="87" y="64" class="brand-word" text-anchor="middle">QUARVEX</text>
</svg></div>
<div class="slide" style="left:804px;top:38px"><svg viewBox="0 0 175 130">
  <rect width="175" height="130" fill="url(#tower)" role="img" aria-label="Glass tower against sky photo"/>
  <rect y="80" width="175" height="50" fill="#1f4a8f"/>
  <circle cx="87" cy="62" r="27" fill="#fff"/>
  <text x="87" y="64" class="brand-word" text-anchor="middle">QUARVEX</text>
  <text x="87" y="104" class="cover-text">ENTER YOUR PRESENTATION TITLE</text>
</svg></div>
<div class="slide" style="left:973px;top:38px"><svg viewBox="0 0 175 130">
  <rect width="175" height="130" fill="url(#tower)" role="img" aria-label="Harbour city and bridge photo"/>
  <polygon points="0,28 165,20 160,50 0,56" fill="#2a4f8f"/>
  <text x="87" y="36" class="cover-text">ENTER YOUR</text><text x="87" y="43" class="cover-text">PRESENTATION TITLE</text>
  <path d="M0,92 H82 A12,12 0 0 1 82,116 H0Z" fill="#fff"/>
  <text x="8" y="106" class="brand-word">QUARVEX</text>
</svg></div>

<!-- Row 2 -->
<div class="slide" style="left:126px;top:162px"><svg viewBox="0 0 175 130">
  <rect width="175" height="130" fill="url(#tower)" role="img" aria-label="Skyscraper viewed from below photo"/>
  <text x="87" y="74" class="cover-text" style="font-size:7px">Introduction</text>
  <rect x="30" y="80" width="115" height="1" fill="#fff" opacity=".6"/><rect x="35" y="84" width="105" height="1" fill="#fff" opacity=".6"/>
  <rect x="40" y="88" width="95" height="1" fill="#fff" opacity=".6"/>
</svg></div>
<div class="slide" style="left:295px;top:162px"><svg viewBox="0 0 175 130">
  <rect width="175" height="130" fill="#1e3459"/>
  <polygon points="70,0 175,0 175,130 95,130" fill="url(#tower)" role="img" aria-label="Glass skyscraper photo"/>
  <circle cx="30" cy="48" r="5" fill="none" stroke="#fff" stroke-width="1.2"/>
  <text x="22" y="70" style="font-size:8px;fill:#fff;font-weight:700">SLIDE TITLE</text>
  <text x="22" y="82" style="font-size:4.5px;fill:#cfd8e6">Your great headline</text>
  <text x="22" y="88" style="font-size:4.5px;fill:#cfd8e6">Lorem Ipsum</text>
</svg></div>
<div class="slide" style="left:465px;top:162px"><svg viewBox="0 0 175 130">
  <use href="#chrome" width="175" height="130"/>
  <text x="9" y="11" class="heading">Design Idea</text><text x="110" y="27" class="subhead">About Us</text>
  <rect x="10" y="38" width="55" height="57" fill="#b5b5b5" role="img" aria-label="Team photo"/>
  <circle cx="90" cy="45" r="5" class="fill-red"/><circle cx="140" cy="45" r="5" class="fill-orange"/>
  <circle cx="90" cy="75" r="5" class="fill-green"/><circle cx="140" cy="75" r="5" class="fill-blue"/>
  <rect x="78" y="54" width="24" height="1" class="txt"/><rect x="128" y="54" width="24" height="1" class="txt"/>
  <rect x="78" y="84" width="24" height="1" class="txt"/><rect x="128" y="84" width="24" height="1" class="txt"/>
</svg></div>
<div class="slide" style="left:634px;top:162px"><svg viewBox="0 0 175 130">
  <use href="#chrome" width="175" height="130"/>
  <text x="9" y="11" class="heading">Design Idea</text><text x="87" y="27" class="subhead">Bullet List Style - 01</text>
  <g class="txt"><rect x="15" y="36" width="145" height="1"/><rect x="15" y="42" width="140" height="1"/><rect x="15" y="48" width="145" height="1"/>
  <rect x="15" y="54" width="130" height="1"/><rect x="15" y="60" width="145" height="1"/><rect x="15" y="66" width="138" height="1"/>
  <rect x="15" y="72" width="145" height="1"/><rect x="15" y="78" width="120" height="1"/><rect x="15" y="84" width="145" height="1"/>
  <rect x="15" y="90" width="140" height="1"/><rect x="15" y="96" width="110" height="1"/></g>
</svg></div>
<div class="slide" style="left:804px;top:162px"><svg viewBox="0 0 175 130">
  <use href="#chrome" width="175" height="130"/>
  <text x="9" y="11" class="heading">Design Idea</text><text x="87" y="27" class="subhead">Bullet List Style-02</text>
  <g class="txt"><rect x="12" y="36" width="70" height="1"/><rect x="12" y="42" width="65" height="1"/><rect x="12" y="48" width="70" height="1"/>
  <rect x="12" y="60" width="68" height="1"/><rect x="12" y="66" width="70" height="1"/><rect x="12" y="78" width="66" height="1"/>
  <rect x="12" y="84" width="70" height="1"/><rect x="12" y="96" width="60" height="1"/>
  <rect x="95" y="36" width="70" height="1"/><rect x="95" y="42" width="66" height="1"/><rect x="95" y="48" width="70" height="1"/>
  <rect x="95" y="54" width="62" height="1"/><rect x="95" y="66" width="70" height="1"/><rect x="95" y="72" width="68" height="1"/>
  <rect x="95" y="78" width="70" height="1"/><rect x="95" y="90" width="64" height="1"/><rect x="95" y="96" width="70" height="1"/></g>
</svg></div>
<div class="slide" style="left:973px;top:162px"><svg viewBox="0 0 175 130">
  <use href="#chrome" width="175" height="130"/>
  <text x="9" y="11" class="heading">Design Idea</text>
  <rect x="20" y="50" width="7" height="42" class="fill-navy"/><rect x="29" y="60" width="7" height="32" class="fill-green"/>
  <rect x="38" y="44" width="7" height="48" class="fill-red"/><rect x="47" y="66" width="7" height="26" class="fill-yellow"/>
  <rect x="56" y="56" width="7" height="36" class="fill-teal"/><rect x="65" y="62" width="7" height="30" class="fill-orange"/>
  <circle cx="92" cy="50" r="4" class="fill-purple"/><circle cx="92" cy="63" r="4" class="fill-teal"/><circle cx="92" cy="76" r="4" class="fill-green"/>
  <circle cx="130" cy="50" r="4" class="fill-blue"/><circle cx="130" cy="63" r="4" class="fill-orange"/><circle cx="130" cy="76" r="4" class="fill-red"/>
  <g class="txt"><rect x="99" y="49" width="20" height="1"/><rect x="99" y="62" width="20" height="1"/><rect x="99" y="75" width="20" height="1"/>
  <rect x="137" y="49" width="20" height="1"/><rect x="137" y="62" width="20" height="1"/><rect x="137" y="75" width="20" height="1"/></g>
</svg></div>

<!-- Row 3 -->
<div class="slide" style="left:126px;top:286px"><svg viewBox="0 0 175 130">
  <use href="#chrome" width="175" height="130"/>
  <text x="9" y="11" class="heading">Design Idea</text>
  <g fill="none" stroke-width="9"><circle cx="87" cy="65" r="18" stroke="var(--red)" stroke-dasharray="28 200"/>
  <circle cx="87" cy="65" r="18" stroke="var(--orange)" stroke-dasharray="0 28 28 200"/>
  <circle cx="87" cy="65" r="18" stroke="var(--green)" stroke-dasharray="0 56 30 200"/>
  <circle cx="87" cy="65" r="18" stroke="var(--teal)" stroke-dasharray="0 86 27 200"/></g>
  <circle cx="50" cy="45" r="5" class="fill-red"/><circle cx="125" cy="45" r="5" class="fill-orange"/>
  <circle cx="50" cy="85" r="5" class="fill-green"/><circle cx="125" cy="85" r="5" class="fill-teal"/>
  <g class="txt"><rect x="12" y="44" width="30" height="1"/><rect x="133" y="44" width="30" height="1"/><rect x="12" y="84" width="30" height="1"/><rect x="133" y="84" width="30" height="1"/></g>
</svg></div>
<div class="slide" style="left:295px;top:286px"><svg viewBox="0 0 175 130">
  <use href="#chrome" width="175" height="130"/>
  <text x="9" y="11" class="heading">Design Idea</text>
  <g fill="none" stroke-width="3"><circle cx="28" cy="52" r="11" stroke="#eee"/><circle cx="28" cy="52" r="11" stroke="var(--green)" stroke-dasharray="17 100"/>
  <circle cx="68" cy="52" r="11" stroke="#eee"/><circle cx="68" cy="52" r="11" stroke="var(--green)" stroke-dasharray="21 100"/>
  <circle cx="108" cy="52" r="11" stroke="#eee"/><circle cx="108" cy="52" r="11" stroke="var(--orange)" stroke-dasharray="35 100"/>
  <circle cx="148" cy="52" r="11" stroke="#eee"/><circle cx="148" cy="52" r="11" stroke="var(--red)" stroke-dasharray="62 100"/></g>
  <rect x="9" y="70" width="157" height="8" fill="#2b7a96"/>
  <g class="txt"><rect x="14" y="84" width="28" height="1"/><rect x="54" y="84" width="28" height="1"/><rect x="94" y="84" width="28" height="1"/><rect x="134" y="84" width="28" height="1"/></g>
</svg></div>
<div class="slide" style="left:465px;top:286px"><svg viewBox="0 0 175 130">
  <use href="#chrome" width="175" height="130"/>
  <text x="9" y="11" class="heading">Design Idea</text>
  <g><rect x="14" y="70" width="4" height="20" class="fill-navy"/><rect x="19" y="62" width="4" height="28" class="fill-green"/><rect x="24" y="74" width="4" height="16" class="fill-orange"/><rect x="29" y="58" width="4" height="32" class="fill-red"/>
  <rect x="52" y="64" width="4" height="26" class="fill-navy"/><rect x="57" y="54" width="4" height="36" class="fill-green"/><rect x="62" y="70" width="4" height="20" class="fill-orange"/><rect x="67" y="60" width="4" height="30" class="fill-red"/>
  <rect x="90" y="56" width="4" height="34" class="fill-navy"/><rect x="95" y="68" width="4" height="22" class="fill-green"/><rect x="100" y="50" width="4" height="40" class="fill-orange"/><rect x="105" y="64" width="4" height="26" class="fill-red"/>
  <rect x="128" y="66" width="4" height="24" class="fill-navy"/><rect x="133" y="60" width="4" height="30" class="fill-green"/><rect x="138" y="56" width="4" height="34" class="fill-orange"/><rect x="143" y="52" width="4" height="38" class="fill-red"/></g>
</svg></div>
<div class="slide" style="left:634px;top:286px"><svg viewBox="0 0 175 130">
  <use href="#chrome" width="175" height="130"/>
  <text x="9" y="11" class="heading">Design Idea</text>
  <rect x="62" y="42" width="10" height="4" fill="#666"/>
  <rect x="28" y="72" width="6" height="22" class="fill-orange"/><rect x="37" y="62" width="6" height="32" class="fill-red"/>
  <rect x="46" y="58" width="6" height="36" class="fill-orange"/><rect x="55" y="52" width="6" height="42" class="fill-yellow"/>
  <rect x="64" y="48" width="6" height="46" class="fill-red"/><rect x="73" y="66" width="6" height="28" class="fill-green"/>
  <g><rect x="100" y="38" width="4" height="4" class="fill-red"/><rect x="100" y="50" width="4" height="4" class="fill-red"/><rect x="100" y="62" width="4" height="4" class="fill-orange"/>
  <rect x="100" y="74" width="4" height="4" class="fill-green"/><rect x="100" y="86" width="4" height="4" class="fill-green"/></g>
  <g class="txt"><rect x="108" y="40" width="50" height="1"/><rect x="108" y="52" width="50" height="1"/><rect x="108" y="64" width="50" height="1"/><rect x="108" y="76" width="50" height="1"/><rect x="108" y="88" width="50" height="1"/></g>
</svg></div>
<div class="slide" style="left:804px;top:286px"><svg viewBox="0 0 175 130">
  <use href="#chrome" width="175" height="130"/>
  <text x="9" y="11" class="heading">Design Idea</text>
  <rect x="18" y="58" width="6" height="30" class="fill-blue"/><rect x="25" y="48" width="6" height="40" class="fill-orange"/><rect x="32" y="62" width="6" height="26" class="fill-yellow"/>
  <rect x="45" y="50" width="6" height="38" class="fill-blue"/><rect x="52" y="56" width="6" height="32" class="fill-orange"/><rect x="59" y="44" width="6" height="44" class="fill-sky"/>
  <rect x="72" y="60" width="6" height="28" class="fill-orange"/><rect x="79" y="52" width="6" height="36" class="fill-blue"/>
  <rect x="98" y="44" width="60" height="3" class="fill-grey"/>
  <rect x="98" y="60" width="60" height="14" fill="#d5d5d5"/>
  <g class="txt"><rect x="98" y="52" width="60" height="1"/><rect x="98" y="56" width="50" height="1"/><rect x="98" y="80" width="60" height="1"/></g>
  <rect x="20" y="96" width="10" height="2" class="fill-navy"/><rect x="45" y="96" width="10" height="2" class="fill-navy"/>
  <rect x="100" y="96" width="10" height="2" class="fill-navy"/><rect x="130" y="96" width="10" height="2" class="fill-navy"/>
</svg></div>
<div class="slide" style="left:973px;top:286px"><svg viewBox="0 0 175 130">
  <use href="#chrome" width="175" height="130"/>
  <text x="9" y="11" class="heading">Design Idea</text>
  <g><rect x="14" y="72" width="4" height="18" class="fill-green"/><rect x="19" y="64" width="4" height="26" class="fill-teal"/><rect x="24" y="70" width="4" height="20" class="fill-navy"/><rect x="29" y="60" width="4" height="30" class="fill-red"/>
  <rect x="52" y="62" width="4" height="28" class="fill-green"/><rect x="57" y="56" width="4" height="34" class="fill-yellow"/><rect x="62" y="68" width="4" height="22" class="fill-navy"/><rect x="67" y="64" width="4" height="26" class="fill-red"/>
  <rect x="90" y="58" width="4" height="32" class="fill-green"/><rect x="95" y="52" width="4" height="38" class="fill-orange"/><rect x="100" y="66" width="4" height="24" class="fill-navy"/><rect x="105" y="60" width="4" height="30" class="fill-red"/>
  <rect x="128" y="68" width="4" height="22" class="fill-green"/><rect x="133" y="60" width="4" height="30" class="fill-yellow"/><rect x="138" y="56" width="4" height="34" class="fill-navy"/><rect x="143" y="50" width="4" height="40" class="fill-red"/></g>
</svg></div>

<!-- Row 4 -->
<div class="slide" style="left:126px;top:410px"><svg viewBox="0 0 175 130">
  <use href="#chrome" width="175" height="130"/>
  <text x="9" y="11" class="heading">Design Idea</text>
  <g><rect x="34" y="52" width="8" height="42" rx="2" class="fill-blue"/><rect x="48" y="60" width="8" height="34" rx="2" class="fill-orange"/>
  <rect x="62" y="70" width="8" height="24" rx="2" class="fill-yellow"/><rect x="76" y="66" width="8" height="28" rx="2" class="fill-grey"/>
  <rect x="90" y="58" width="8" height="36" rx="2" class="fill-navy"/><rect x="104" y="68" width="8" height="26" rx="2" class="fill-orange"/>
  <rect x="118" y="62" width="8" height="32" rx="2" class="fill-yellow"/><rect x="132" y="48" width="8" height="46" rx="2" fill="#999"/></g>
  <rect x="28" y="94" width="118" height="3" fill="#ccc"/>
</svg></div>
<div class="slide" style="left:295px;top:410px"><svg viewBox="0 0 175 130">
  <use href="#chrome" width="175" height="130"/>
  <text x="9" y="11" class="heading">Table Style</text>
  <rect x="14" y="40" width="38" height="7" class="fill-navy"/><rect x="52" y="40" width="36" height="7" class="fill-orange"/>
  <rect x="88" y="40" width="36" height="7" class="fill-green"/><rect x="124" y="40" width="36" height="7" class="fill-orange"/>
  <g class="fill-grey"><rect x="14" y="50" width="146" height="4" opacity=".6"/><rect x="14" y="60" width="146" height="4" opacity=".6"/><rect x="14" y="70" width="146" height="4" opacity=".6"/><rect x="14" y="80" width="146" height="4" opacity=".6"/></g>
  <g fill="none" stroke="var(--green)" stroke-width=".8"><circle cx="106" cy="52" r="2"/><circle cx="106" cy="62" r="2"/><circle cx="106" cy="72" r="2"/><circle cx="106" cy="82" r="2"/><circle cx="142" cy="57" r="2" stroke="var(--orange)"/><circle cx="142" cy="77" r="2" stroke="var(--orange)"/></g>
</svg></div>
<div class="slide" style="left:465px;top:410px"><svg viewBox="0 0 175 130">
  <use href="#chrome" width="175" height="130"/>
  <text x="9" y="11" class="heading">Table Style - 02</text>
  <rect x="44" y="36" width="28" height="6" class="fill-sky"/><rect x="73" y="36" width="28" height="6" class="fill-orange"/>
  <rect x="102" y="36" width="28" height="6" class="fill-orange"/><rect x="131" y="36" width="28" height="6" class="fill-yellow"/>
  <g class="txt"><rect x="14" y="48" width="22" height="1"/><rect x="14" y="56" width="22" height="1"/><rect x="14" y="64" width="22" height="1"/><rect x="14" y="72" width="22" height="1"/><rect x="14" y="80" width="22" height="1"/></g>
  <g fill="none" stroke="var(--red)" stroke-width=".7"><circle cx="58" cy="48" r="1.8"/><circle cx="87" cy="56" r="1.8"/><circle cx="116" cy="48" r="1.8"/><circle cx="145" cy="64" r="1.8"/><circle cx="87" cy="72" r="1.8"/><circle cx="116" cy="80" r="1.8"/></g>
</svg></div>
<div class="slide" style="left:634px;top:410px"><svg viewBox="0 0 175 130">
  <use href="#chrome" width="175" height="130"/>
  <text x="9" y="11" class="heading">Table Style - 03</text>
  <rect x="44" y="36" width="28" height="6" class="fill-sky"/><rect x="73" y="36" width="28" height="6" class="fill-orange"/>
  <rect x="102" y="36" width="28" height="6" class="fill-blue"/><rect x="131" y="36" width="28" height="6" class="fill-yellow"/>
  <g class="txt"><rect x="14" y="48" width="22" height="1"/><rect x="14" y="56" width="22" height="1"/><rect x="14" y="64" width="22" height="1"/><rect x="14" y="72" width="22" height="1"/><rect x="14" y="80" width="22" height="1"/></g>
  <g fill="none" stroke="var(--red)" stroke-width=".7"><circle cx="58" cy="56" r="1.8"/><circle cx="87" cy="48" r="1.8"/><circle cx="145" cy="56" r="1.8"/><circle cx="116" cy="72" r="1.8"/><circle cx="145" cy="80" r="1.8"/></g>
</svg></div>
<div class="slide" style="left:804px;top:410px"><svg viewBox="0 0 175 130">
  <use href="#chrome" width="175" height="130"/>
  <text x="9" y="11" class="heading">Table Style - 04</text>
  <rect x="14" y="36" width="58" height="6" class="fill-red"/><rect x="72" y="36" width="22" height="6" class="fill-orange"/>
  <rect x="94" y="36" width="22" height="6" class="fill-yellow"/><rect x="116" y="36" width="22" height="6" class="fill-blue"/><rect x="138" y="36" width="22" height="6" class="fill-sky"/>
  <g class="txt"><rect x="20" y="48" width="40" height="1"/><rect x="20" y="54" width="40" height="1"/><rect x="20" y="60" width="40" height="1"/><rect x="20" y="66" width="40" height="1"/><rect x="20" y="72" width="40" height="1"/>
  <rect x="78" y="48" width="10" height="1"/><rect x="100" y="54" width="10" height="1"/><rect x="122" y="60" width="10" height="1"/><rect x="144" y="66" width="10" height="1"/></g>
  <rect x="14" y="78" width="146" height=".8" fill="#555"/>
</svg></div>
<div class="slide" style="left:973px;top:410px"><svg viewBox="0 0 175 130">
  <use href="#chrome" width="175" height="130"/>
  <text x="9" y="11" class="heading">Design Idea</text>
  <g fill="none" stroke-width="1"><polyline points="20,95 50,90 80,86 110,70 140,60 160,55" stroke="var(--red)"/>
  <polyline points="20,96 50,94 80,92 110,84 140,78 160,74" stroke="var(--orange)"/>
  <polyline points="20,97 50,95 80,96 110,92 140,90 160,88" stroke="var(--teal)"/></g>
  <rect x="20" y="98" width="140" height=".6" fill="#ccc"/>
</svg></div>

<!-- Row 5 -->
<div class="slide" style="left:126px;top:534px"><svg viewBox="0 0 175 130">
  <use href="#chrome" width="175" height="130"/>
  <text x="9" y="11" class="heading">Design Idea</text>
  <rect x="12" y="34" width="95" height="64" fill="#f3f3f3"/>
  <g fill="none" stroke-width=".9"><polyline points="18,88 34,80 50,84 66,70 82,74 98,58" stroke="var(--orange)"/>
  <polyline points="18,92 34,86 50,78 66,82 82,66 98,62" stroke="var(--blue)"/></g>
  <g fill="none" stroke-width="3"><circle cx="120" cy="52" r="8" stroke="var(--blue)"/><circle cx="150" cy="52" r="8" stroke="var(--orange)"/>
  <circle cx="120" cy="80" r="8" stroke="#999"/><circle cx="150" cy="80" r="8" stroke="var(--yellow)"/></g>
</svg></div>
<div class="slide" style="left:295px;top:534px"><svg viewBox="0 0 175 130">
  <use href="#chrome" width="175" height="130"/>
  <text x="9" y="11" class="heading">Design Idea</text>
  <g><rect x="14" y="42" width="50" height="3" class="fill-orange"/><rect x="14" y="46" width="60" height="3" class="fill-red"/><rect x="14" y="50" width="40" height="3" class="fill-blue"/>
  <rect x="14" y="58" width="70" height="3" class="fill-green"/><rect x="14" y="62" width="44" height="3" class="fill-yellow"/><rect x="14" y="66" width="58" height="3" class="fill-blue"/>
  <rect x="14" y="74" width="36" height="3" class="fill-red"/><rect x="14" y="78" width="64" height="3" class="fill-orange"/><rect x="14" y="82" width="48" height="3" class="fill-navy"/></g>
  <circle cx="120" cy="44" r="4" class="fill-red"/><circle cx="120" cy="58" r="4" class="fill-orange"/><circle cx="120" cy="72" r="4" class="fill-green"/><circle cx="120" cy="86" r="4" class="fill-blue"/>
  <g class="txt"><rect x="128" y="43" width="30" height="1"/><rect x="128" y="57" width="30" height="1"/><rect x="128" y="71" width="30" height="1"/><rect x="128" y="85" width="30" height="1"/></g>
</svg></div>
<div class="slide" style="left:465px;top:534px"><svg viewBox="0 0 175 130">
  <use href="#chrome" width="175" height="130"/>
  <text x="9" y="11" class="heading">Design Idea</text>
  <g><rect x="14" y="40" width="30" height="3" class="fill-orange"/><rect x="14" y="46" width="36" height="3" class="fill-red"/><rect x="14" y="52" width="24" height="3" class="fill-orange"/><rect x="14" y="58" width="40" height="3" class="fill-red"/>
  <rect x="96" y="40" width="22" height="3" class="fill-teal"/><rect x="96" y="46" width="30" height="3" class="fill-blue"/><rect x="96" y="52" width="18" height="3" class="fill-teal"/><rect x="96" y="58" width="26" height="3" class="fill-blue"/></g>
  <rect x="12" y="75" width="70" height="20" class="fill-teal"/><text x="16" y="89" class="figure">34%</text>
  <rect x="94" y="75" width="70" height="20" class="fill-teal"/><text x="98" y="89" class="figure">12%</text>
</svg></div>
<div class="slide" style="left:634px;top:534px"><svg viewBox="0 0 175 130">
  <use href="#chrome" width="175" height="130"/>
  <text x="9" y="11" class="heading">Design Idea</text>
  <polygon points="12,38 42,38 50,50 42,62 12,62 20,50" class="fill-blue"/>
  <polygon points="50,38 80,38 88,50 80,62 50,62 58,50" class="fill-green"/>
  <polygon points="88,38 118,38 126,50 118,62 88,62 96,50" class="fill-orange"/>
  <polygon points="126,38 156,38 164,50 156,62 126,62 134,50" class="fill-red"/>
  <g class="txt"><rect x="16" y="72" width="30" height="1"/><rect x="16" y="76" width="26" height="1"/><rect x="54" y="72" width="30" height="1"/><rect x="54" y="76" width="26" height="1"/>
  <rect x="92" y="72" width="30" height="1"/><rect x="92" y="76" width="26" height="1"/><rect x="130" y="72" width="30" height="1"/><rect x="130" y="76" width="26" height="1"/></g>
</svg></div>
<div class="slide" style="left:804px;top:534px"><svg viewBox="0 0 175 130">
  <use href="#chrome" width="175" height="130"/>
  <text x="9" y="11" class="heading">Design Idea</text>
  <polygon points="18,82 29,72 40,82 40,98 18,98" fill="#2a5d8f"/>
  <polygon points="56,72 68,60 80,72 80,98 56,98" class="fill-teal"/>
  <polygon points="96,60 108,46 120,60 120,98 96,98" class="fill-green"/>
  <polygon points="136,50 148,36 160,50 160,98 136,98" class="fill-orange"/>
  <rect x="22" y="64" width="9" height="5" class="fill-red"/><rect x="62" y="52" width="9" height="5" class="fill-red"/><rect x="102" y="38" width="9" height="5" class="fill-red"/>
</svg></div>
<div class="slide" style="left:973px;top:534px"><svg viewBox="0 0 175 130">
  <use href="#chrome" width="175" height="130"/>
  <text x="9" y="11" class="heading">Design Idea</text>
  <g><rect x="18" y="62" width="5" height="26" class="fill-navy"/><rect x="25" y="56" width="5" height="32" class="fill-green"/><rect x="32" y="66" width="5" height="22" class="fill-red"/><rect x="39" y="58" width="5" height="30" class="fill-navy"/><rect x="46" y="52" width="5" height="36" class="fill-green"/><rect x="53" y="60" width="5" height="28" class="fill-red"/><rect x="60" y="48" width="5" height="40" class="fill-navy"/><rect x="67" y="64" width="5" height="24" class="fill-red"/>
  <rect x="98" y="64" width="5" height="24" class="fill-navy"/><rect x="105" y="58" width="5" height="30" class="fill-orange"/><rect x="112" y="54" width="5" height="34" class="fill-red"/><rect x="119" y="62" width="5" height="26" class="fill-navy"/><rect x="126" y="50" width="5" height="38" class="fill-orange"/><rect x="133" y="58" width="5" height="30" class="fill-red"/><rect x="140" y="46" width="5" height="42" class="fill-navy"/><rect x="147" y="60" width="5" height="28" class="fill-red"/></g>
</svg></div>

<!-- Row 6 -->
<div class="slide" style="left:126px;top:658px"><svg viewBox="0 0 175 130">
  <use href="#chrome" width="175" height="130"/>
  <text x="9" y="11" class="heading">Design Idea</text>
  <g><rect x="14" y="40" width="30" height="3" class="fill-orange"/><rect x="14" y="46" width="36" height="3" class="fill-red"/><rect x="14" y="52" width="24" height="3" class="fill-orange"/><rect x="14" y="58" width="40" height="3" class="fill-red"/>
  <rect x="96" y="40" width="22" height="3" class="fill-teal"/><rect x="96" y="46" width="30" height="3" class="fill-blue"/><rect x="96" y="52" width="18" height="3" class="fill-teal"/><rect x="96" y="58" width="26" height="3" class="fill-blue"/></g>
  <rect x="12" y="75" width="70" height="20" class="fill-teal"/><text x="16" y="89" class="figure">34%</text>
  <rect x="94" y="75" width="70" height="20" class="fill-teal"/><text x="98" y="89" class="figure">12%</text>
</svg></div>
<div class="slide" style="left:295px;top:658px"><svg viewBox="0 0 175 130">
  <use href="#chrome" width="175" height="130"/>
  <text x="9" y="11" class="heading">Design Idea</text>
  <polygon points="22,90 28,58 34,90" class="fill-navy"/><circle cx="28" cy="54" r="4" class="fill-navy"/>
  <polygon points="44,90 50,62 56,90" class="fill-sky"/><circle cx="50" cy="58" r="4" class="fill-sky"/>
  <polygon points="66,90 72,54 78,90" class="fill-green"/><circle cx="72" cy="50" r="4" class="fill-green"/>
  <polygon points="88,90 94,58 100,90" class="fill-yellow"/><circle cx="94" cy="54" r="4" class="fill-yellow"/>
  <polygon points="110,90 116,50 122,90" class="fill-orange"/><circle cx="116" cy="46" r="4" class="fill-orange"/>
  <polygon points="132,90 138,40 144,90" class="fill-red"/><circle cx="138" cy="36" r="4" class="fill-red"/>
  <rect x="16" y="90" width="140" height=".6" fill="#bbb"/>
</svg></div>
<div class="slide" style="left:465px;top:658px"><svg viewBox="0 0 175 130">
  <use href="#chrome" width="175" height="130"/>
  <text x="9" y="11" class="heading">Design Idea</text>
  <g opacity=".8"><path d="M10,92 C28,92 30,52 42,52 C54,52 56,92 74,92Z" fill="#6fc4d6"/>
  <path d="M40,92 C58,92 60,48 72,48 C84,48 86,92 104,92Z" fill="#a6d37a"/>
  <path d="M70,92 C88,92 90,46 102,46 C114,46 116,92 134,92Z" fill="#f5c96b"/>
  <path d="M100,92 C118,92 120,50 132,50 C144,50 146,92 164,92Z" fill="#ef8e78"/></g>
</svg></div>
<div class="slide" style="left:634px;top:658px"><svg viewBox="0 0 175 130">
  <use href="#chrome" width="175" height="130"/>
  <text x="9" y="11" class="heading">Design Idea</text>
  <circle cx="34" cy="64" r="20" class="fill-teal"/>
  <circle cx="58" cy="48" r="4" class="fill-green"/><circle cx="60" cy="62" r="4" class="fill-green"/><circle cx="58" cy="76" r="4" class="fill-teal"/>
  <g class="txt"><rect x="66" y="47" width="26" height="1"/><rect x="68" y="61" width="26" height="1"/><rect x="66" y="75" width="26" height="1"/></g>
  <rect x="110" y="38" width="50" height="26" fill="#34506e"/><rect x="110" y="68" width="50" height="26" fill="#34506e"/>
</svg></div>
<div class="slide" style="left:804px;top:658px"><svg viewBox="0 0 175 130">
  <use href="#chrome" width="175" height="130"/>
  <text x="9" y="11" class="heading">Design Idea</text>
  <g class="fill-green"><rect x="20" y="64" width="5" height="30"/><rect x="40" y="70" width="5" height="24"/><rect x="60" y="58" width="5" height="36"/>
  <rect x="80" y="66" width="5" height="28"/><rect x="100" y="54" width="5" height="40"/><rect x="120" y="62" width="5" height="32"/><rect x="140" y="48" width="5" height="46"/></g>
  <circle cx="22.5" cy="54" r="4" class="fill-teal"/><circle cx="42.5" cy="60" r="4" class="fill-teal"/><circle cx="62.5" cy="48" r="4" class="fill-teal"/>
  <circle cx="82.5" cy="56" r="4" class="fill-teal"/><circle cx="102.5" cy="44" r="4" class="fill-teal"/><circle cx="122.5" cy="52" r="4" class="fill-teal"/><circle cx="142.5" cy="38" r="4" class="fill-teal"/>
</svg></div>
<div class="slide" style="left:973px;top:658px"><svg viewBox="0 0 175 130">
  <use href="#chrome" width="175" height="130"/>
  <text x="9" y="11" class="heading">Design Idea</text>
  <g fill="none" stroke-width="9"><circle cx="87" cy="64" r="18" stroke="var(--red)" stroke-dasharray="28 200"/>
  <circle cx="87" cy="64" r="18" stroke="var(--orange)" stroke-dasharray="0 28 28 200"/>
  <circle cx="87" cy="64" r="18" stroke="var(--yellow)" stroke-dasharray="0 56 30 200"/>
  <circle cx="87" cy="64" r="18" stroke="var(--teal)" stroke-dasharray="0 86 27 200"/></g>
  <circle cx="20" cy="48" r="4" fill="none" stroke="var(--teal)"/><circle cx="20" cy="64" r="4" fill="none" stroke="var(--teal)"/><circle cx="20" cy="80" r="4" fill="none" stroke="var(--teal)"/>
  <text x="134" y="46" class="big-pct">35%</text><text x="134" y="84" class="big-pct">15%</text>
</svg></div>

<!-- Row 7 -->
<div class="slide" style="left:126px;top:782px"><svg viewBox="0 0 175 130">
  <use href="#chrome" width="175" height="130"/>
  <text x="9" y="11" class="heading">Pie Chart Design Idea</text>
  <ellipse cx="87" cy="66" rx="28" ry="12" class="fill-navy"/>
  <path d="M87,66 L87,54 A28,12 0 0 1 115,66Z" class="fill-red"/>
  <path d="M87,66 L115,66 A28,12 0 0 1 92,78Z" class="fill-green"/>
  <path d="M87,66 L59,66 A28,12 0 0 1 87,54Z" class="fill-orange"/>
  <rect x="12" y="38" width="26" height="14" class="fill-orange"/><rect x="137" y="38" width="26" height="14" class="fill-red"/>
  <rect x="12" y="74" width="26" height="14" class="fill-blue"/><rect x="137" y="74" width="26" height="14" class="fill-green"/>
</svg></div>

<div class="file-name" style="left:126px;top:146px">Slide1.JPG</div>
<div class="file-name" style="left:295px;top:146px">Slide2.JPG</div>
<div class="file-name" style="left:465px;top:146px">Slide3.JPG</div>
<div class="file-name" style="left:634px;top:146px">Slide4.JPG</div>
<div class="file-name" style="left:804px;top:146px">Slide5.JPG</div>
<div class="file-name" style="left:973px;top:146px">Slide6.JPG</div>
<div class="file-name" style="left:126px;top:270px">Slide7.JPG</div>
<div class="file-name" style="left:295px;top:270px">Slide8.JPG</div>
<div class="file-name" style="left:465px;top:270px">Slide9.JPG</div>
<div class="file-name" style="left:634px;top:270px">Slide10.JPG</div>
<div class="file-name" style="left:804px;top:270px">Slide11.JPG</div>
<div class="file-name" style="left:973px;top:270px">Slide12.JPG</div>
<div class="file-name" style="left:126px;top:394px">Slide13.JPG</div>
<div class="file-name" style="left:295px;top:394px">Slide14.JPG</div>
<div class="file-name" style="left:465px;top:394px">Slide15.JPG</div>
<div class="file-name" style="left:634px;top:394px">Slide16.JPG</div>
<div class="file-name" style="left:804px;top:394px">Slide17.JPG</div>
<div class="file-name" style="left:973px;top:394px">Slide18.JPG</div>
<div class="file-name" style="left:126px;top:518px">Slide19.JPG</div>
<div class="file-name" style="left:295px;top:518px">Slide20.JPG</div>
<div class="file-name" style="left:465px;top:518px">Slide21.JPG</div>
<div class="file-name" style="left:634px;top:518px">Slide22.JPG</div>
<div class="file-name" style="left:804px;top:518px">Slide23.JPG</div>
<div class="file-name" style="left:973px;top:518px">Slide24.JPG</div>
<div class="file-name" style="left:126px;top:642px">Slide25.JPG</div>
<div class="file-name" style="left:295px;top:642px">Slide26.JPG</div>
<div class="file-name" style="left:465px;top:642px">Slide27.JPG</div>
<div class="file-name" style="left:634px;top:642px">Slide28.JPG</div>
<div class="file-name" style="left:804px;top:642px">Slide29.JPG</div>
<div class="file-name" style="left:973px;top:642px">Slide30.JPG</div>
<div class="file-name" style="left:126px;top:766px">Slide31.JPG</div>
<div class="file-name" style="left:295px;top:766px">Slide32.JPG</div>
<div class="file-name" style="left:465px;top:766px">Slide33.JPG</div>
<div class="file-name" style="left:634px;top:766px">Slide34.JPG</div>
<div class="file-name" style="left:804px;top:766px">Slide35.JPG</div>
<div class="file-name" style="left:973px;top:766px">Slide36.JPG</div>
<div class="file-name" style="left:126px;top:890px">Slide37.JPG</div>

<h1 class="collection-title">SLIDE DESIGN IDEA - 02<br>( With Line Borders on Top &amp; Bottom of Slides)</h1>
</body>
</html>
```